LRV Website

We need a completely new modern design for our website www.lrv.org.au.

The Tenure Holders Alliance of Australia Inc is a non-profit, volunteer-run association representing owners of strata-titled residential developments. We provide education, information and lobbying to improve the management of apartment complexes and the lives of those living in them. We’re all about “owners helping owners”. More information on our organisation can be seen at www.lrv.org.au.

Our new logo (from a recent MarkPanel contest) is attached.

Target Market(s)

Primary audience - Owners of residential apartments - both resident owners and investor owners
Secondary audiences – current and potential sponsors; organisations providing products & services to Owners Corporations & Body Corporates

Industry/Entity Type

Non-Profit

Number of Pages Required

3 pages

Requirements
Must have
• We need:
- A design for the home page
- A design for 2-column content pages
- Fonts and colours for
* standard text
* H1, H2, H3 and H4 heading tags
* Bulleted and numbered lists
- A complementary colour scheme for the Calendar page
- A complementary breadcrumb format
- A standard format to display the associated tags for any content page

The above are described in more detail in the attached document.

The design should:
- be modern, uncluttered and clean
- reflect a sense of community, coupled with authority, professionalism and knowledge
- be a fixed width of 1000px

At a minimum the files we need are:
- The source file (PSD with all component layers is preferred, but not mandatory)
- JPG preview files
- Any stand-alone images as a PNG with transparent backgrounds
- Details of all fonts and sizes used (if they can’t be easily identified in the source files)

Note: The site is built with the Drupal CMS, so all page elements must be able to be clearly isolated.
Should not have
• Any fonts that are not freely available

```html
<!DOCTYPE html>
<html lang="en">
<head>
<meta charset="utf-8">
<title>LRV – Tenure Holders Alliance</title>
<link rel="stylesheet" href="https://fonts.googleapis.com/css2?family=Open+Sans:wght@400;600;700&family=PT+Serif:ital@1&display=swap">
<style>
:root{
  --sky-top:#9fb4c9;
  --sky-mid:#b8c9d8;
  --band-light:#d9e3ea;
  --body-blue:#7f98b6;
  --panel-edge:#b3c3d6;
  --white:#ffffff;
  --navy:#1f3a72;
  --text-navy:#203870;
  --gold:#d4922a;
  --footer-mid:#3e5c8c;
  --footer-dark:#1e3870;
  --side-head:#a9bacd;
  --chirp-blue:#3a7fb0;
}
*{box-sizing:border-box;margin:0;padding:0}
html,body{width:1200px;height:900px;overflow:hidden}
body{font-family:"Open Sans",sans-serif;color:var(--text-navy);background:var(--body-blue);position:relative}
.header{position:absolute;left:0;top:0;width:1200px;height:222px;
  background:linear-gradient(180deg,var(--sky-top) 0%,var(--sky-mid) 70%,var(--band-light) 89%,var(--sky-mid) 100%)}
.brand{position:absolute;left:868px;top:30px;display:flex;align-items:center;gap:12px}
.brand-mark{width:62px;height:62px;background:var(--gold);border-radius:50%}
.brand-name{font-size:23px;line-height:24px;font-weight:600;color:var(--navy);letter-spacing:.5px}
.nav{position:absolute;left:18px;top:119px;width:911px;height:50px;display:flex;
  background:linear-gradient(180deg,#f3f6f8,#cfd9e2);border:1px solid #e6edf2;border-radius:8px;box-shadow:0 2px 3px rgba(40,60,90,.3)}
.nav a{display:flex;align-items:center;justify-content:center;font-size:14.5px;color:#2c3e55;text-decoration:none;letter-spacing:.5px;border-right:1px solid #bccad6;height:100%}
.nav a:last-child{border-right:none}
.search{position:absolute;left:958px;top:162px;display:flex;align-items:center;gap:8px}
.search input{width:166px;height:28px;border:1px solid #8ea1b5;background:var(--white)}
.search span{font-size:14px;font-weight:700;color:var(--navy);letter-spacing:1px}
.content{position:absolute;left:14px;top:232px;width:773px;height:488px;background:var(--panel-edge);border-radius:18px;padding:8px 10px}
.content-inner{background:var(--white);border-radius:16px;height:100%;padding:10px 14px}
.content h1{font-size:22px;color:var(--gold);font-weight:700;letter-spacing:1px;margin-bottom:14px}
.tagline{font-size:13.5px;font-weight:700;line-height:17px;margin-bottom:17px;letter-spacing:.4px}
.content p{font-size:13.5px;line-height:17px;margin-bottom:17px;letter-spacing:.2px}
.side-head{position:absolute;left:830px;width:317px;height:36px;background:var(--side-head);border-radius:8px;display:flex;align-items:center}
.side-head .dot{width:24px;height:24px;border-radius:50%;background:#dbe4ec;margin:0 30px 0 12px}
.side-head h2{font-size:18px;font-weight:400;color:var(--navy);letter-spacing:1px}
.login label{position:absolute;left:844px;font-size:13px;font-weight:700;color:var(--white);letter-spacing:.6px}
.login input{position:absolute;left:858px;width:271px;height:28px;border:1px solid #56708f;background:var(--white)}
.pill{position:absolute;height:22px;border-radius:11px;background:linear-gradient(180deg,#fff,#d9dfe5);color:var(--gold);font-size:12px;font-weight:700;display:flex;align-items:center;justify-content:center;letter-spacing:1px}
.rule{position:absolute;left:832px;top:462px;width:316px;height:1px;background:var(--white)}
.events{position:absolute;left:828px;top:530px;width:317px;height:166px;background:#a4b6ca;border-radius:8px;padding:12px 8px}
.events-inner{background:var(--white);border-radius:10px;height:100%;padding:8px 10px;font-size:13px;line-height:17px}
.chirp-bird{position:absolute;left:708px;top:732px;width:66px;height:54px;background:var(--chirp-blue);border-radius:50% 40% 50% 20%}
.chirp-bubble{position:absolute;left:774px;top:736px;width:217px;height:32px;background:var(--chirp-blue);border-radius:6px;color:var(--white);font-size:17px;display:flex;align-items:center;justify-content:center;letter-spacing:.5px}
.footer{position:absolute;left:0;top:778px;width:1200px;height:68px;background:var(--footer-mid)}
.footer-base{position:absolute;left:0;top:846px;width:1200px;height:54px;background:var(--footer-dark)}
.copyright{position:absolute;left:26px;top:815px;font-size:15px;font-weight:700;color:var(--white)}
.footer-links{position:absolute;left:412px;top:813px;font-size:15px;font-weight:700;color:var(--white)}
.footer-links a{color:var(--white);text-decoration:none}
.tweet{position:absolute;left:744px;top:788px;width:452px;font-family:"PT Serif",serif;font-style:italic;font-size:16px;line-height:23px;color:var(--white);letter-spacing:.4px}
.tweet a{color:var(--white)}
</style>
</head>
<body>
<header class="header">
  <div class="brand"><span class="brand-mark"></span><span class="brand-name">TENURE<br>HOLDERS<br>ALLIANCE</span></div>
  <nav class="nav">
    <a style="width:97px">HOME</a><a style="width:103px">ABOUT US</a><a style="width:74px">NEWS</a><a style="width:91px">EVENTS</a><a style="width:102px">CONTACT</a><a style="width:118px">MEMBERSHIP</a><a style="width:122px">SPONSORSHIP</a><a style="width:66px">LINKS</a><a style="width:136px">MEMBERS ONLY</a>
  </nav>
  <form class="search"><input type="text" aria-label="Search"><span>search</span></form>
</header>

<main class="content">
  <div class="content-inner">
    <h1>Tenure Holders Alliance</h1>
    <p class="tagline">... owners helping owners<br>... representing strata title residential developments<br>... lobbying and sharing information to improve apartment living</p>
    <p>The Tenure Holders Alliance of Australia (LRV) is the peak body representing apartment owners, with most members drawn from Owners Corporations' Executive Committees (ECs) or concerned apartment owners around Australia. LRV is a not-for-profit association.</p>
    <p>Through representation, lobbying, information-sharing and networking, we perform a vital service for our members that supports them in living in and/or investing in strata titled property.</p>
    <p>We lobby for changes necessary to Government policy and legislation, and sit on many Government and industry boards and panels to present our views to those in power. The LRV gives members a voice at both State and Federal levels, and an opportunity to put forward their views on problems, solutions and the kind of future that, as apartment owners, we'd all like to see.</p>
    <p>The LRV educates EC members and individuals by sharing experiences and disseminating information from relevant sources and related organisations.</p>
    <p>Regular meetings, seminars and an online discussion group give members access to fellow members' experiences in areas such as defects rectification, strata disputes, shared services, and levy management. These resources may save members thousands of dollars and an immense amount of heartache in the long run!</p>
  </div>
</main>

<aside class="login">
  <div class="side-head" style="top:234px"><span class="dot"></span><h2>MEMBER LOGIN</h2></div>
  <label style="top:280px">Username or email:*</label>
  <input style="top:306px" type="text" aria-label="Username or email">
  <label style="top:346px">Password:*</label>
  <input style="top:371px" type="password" aria-label="Password">
  <div class="pill" style="left:844px;top:412px;width:107px">LOG IN</div>
</aside>
<div class="rule"></div>

<div class="side-head" style="top:486px"><span class="dot"></span><h2>UPCOMING EVENTS</h2></div>
<section class="events"><div class="events-inner">Lorem ipsum dolor sit amet, consectetur adipisicing elit, sed do eiusmod tempor incididunt ut labore et dolore magna aliqua.</div></section>
<div class="pill" style="left:844px;top:704px;width:88px;font-size:11px">read more</div>

<div class="chirp-bird" role="img" aria-label="Small bird illustration beside the follow link"></div>
<div class="chirp-bubble">follow us on Chirper</div>

<footer class="footer"></footer>
<div class="footer-base"></div>
<div class="copyright">Copyright © 2009 Company Name, Inc.</div>
<div class="footer-links"><a>Home</a> &nbsp;|&nbsp; <a>Sitemap</a> &nbsp;|&nbsp; <a>Contact Us</a></div>
<p class="tweet">RT @Lorem ipsum dolor sit amet, consectetur adipisicing elit, sed do eiusmod tempor. <a>http://lnk.to/4Rt8Qa</a></p>
</body>
</html>
```